New Velbrix Business Card Design

We need a business card to match our new branding. The look should utilize the elements as attached here (Vector files & new exec overview are attached.) I really like 'organic' looking elements (e.g. an idea would be to have this printed on recycled paper stock). Thank you! Looking forward to seeing your designs.

Business

```html
<!DOCTYPE html>
<html lang="en">
<head>
<meta charset="utf-8">
<title>Velbrix Business Card</title>
<link rel="stylesheet" href="https://fonts.googleapis.com/css2?family=Questrial&display=swap">
<style>
  :root {
    --brand-blue: #1574bd;
    --brand-green: #8dc63f;
    --card-white: #fbfbfa;
    --backdrop: #d9dadb;
    --card-edge: #2b2b2b;
    --card-shadow: rgba(0, 0, 0, 0.28);
  }
  * { margin: 0; padding: 0; box-sizing: border-box; }
  html, body {
    width: 1200px;
    height: 1000px;
    overflow: hidden;
    background: var(--backdrop);
    font-family: "Questrial", "Century Gothic", sans-serif;
  }
  .canvas {
    position: relative;
    width: 1200px;
    height: 1000px;
  }
  .card {
    position: absolute;
    width: 630px;
    height: 360px;
    background: var(--card-white);
    box-shadow: 4px 6px 0 var(--card-edge), 0 12px 30px var(--card-shadow);
    overflow: hidden;
  }
  .card--front { left: 500px; top: 70px; }
  .card--back  { left: 70px;  top: 540px; }

  /* Front */
  .front-brand {
    position: absolute;
    left: 0; right: 0;
    top: 88px;
    display: flex;
    align-items: center;
    justify-content: center;
    gap: 18px;
  }
  .brand-dot {
    width: 46px; height: 46px;
    border-radius: 50%;
    background: var(--brand-green);
    flex: none;
  }
  .front-brand .brand-name {
    font-size: 104px;
    line-height: 1;
    color: var(--brand-blue);
    letter-spacing: 1px;
  }
  .tagline {
    position: absolute;
    left: 0; right: 0;
    top: 210px;
    text-align: center;
    font-size: 28px;
    color: var(--brand-green);
  }
  .website {
    position: absolute;
    left: 0; right: 0;
    top: 290px;
    text-align: center;
    font-size: 22px;
    color: var(--brand-blue);
    letter-spacing: 0.5px;
  }

  /* Back */
  .back-arcs {
    position: absolute;
    left: 0; top: 0;
    width: 630px; height: 360px;
  }
  .back-content {
    position: absolute;
    left: 200px;
    right: 30px;
    top: 30px;
    text-align: center;
  }
  .back-brand {
    display: flex;
    align-items: center;
    justify-content: center;
    gap: 10px;
    margin-bottom: 28px;
  }
  .back-brand .brand-dot { width: 26px; height: 26px; }
  .back-brand .brand-name {
    font-size: 56px;
    line-height: 1;
    color: var(--brand-blue);
  }
  .person-name {
    font-size: 26px;
    color: var(--brand-blue);
    letter-spacing: 0.5px;
  }
  .person-title {
    font-size: 18px;
    color: var(--brand-green);
    margin-bottom: 22px;
  }
  .contact-list {
    list-style: none;
    font-size: 17px;
    line-height: 1.45;
    color: var(--brand-blue);
  }
  .contact-label { color: var(--brand-green); }
</style>
</head>
<body>
<main class="canvas">

  <section class="card card--front" aria-label="Card front">
    <div class="front-brand">
      <span class="brand-dot"></span>
      <span class="brand-name">velbrix</span>
    </div>
    <p class="tagline">Reach Past Launch Day</p>
    <p class="website">www.velbrix.com</p>
  </section>

  <section class="card card--back" aria-label="Card back">
    <svg class="back-arcs" viewBox="0 0 630 360" aria-hidden="true">
      <path d="M0 0 H150 C60 80 60 270 150 360 H0 Z" fill="var(--brand-green)"/>
      <path d="M120 0 H195 C95 80 95 270 195 360 H120 C30 270 30 80 120 0 Z" fill="var(--brand-blue)"/>
    </svg>
    <div class="back-content">
      <div class="back-brand">
        <span class="brand-dot"></span>
        <span class="brand-name">velbrix</span>
      </div>
      <p class="person-name">YOUR NAME</p>
      <p class="person-title">Title</p>
      <ul class="contact-list">
        <li><span class="contact-label">Phone:</span> 123 456 7890</li>
        <li><span class="contact-label">Mobile:</span> 123 456 7890</li>
        <li><span class="contact-label">Email:</span> yourname@velbrix.com</li>
        <li><span class="contact-label">Address:</span> Street No, Name of City, Country, NY 12345</li>
      </ul>
    </div>
  </section>

</main>
</body>
</html>
```